Sun Path & Clear Way
Use same font as used in my logo
Marla Tenbeck
48207 hwy 19 north dalworth, ar 71482
mltenbeck@mailvox.example
Please change the color of the logo. i will send the color code. Also need changes to letterhead, envelope & card. need asap. thanks.

```html
<!DOCTYPE html>
<html lang="en">
<head>
<meta charset="utf-8">
<title>Sun Path &amp; Clear Way – Stationery Set</title>
<link rel="stylesheet" href="https://fonts.googleapis.com/css2?family=Nunito:wght@400;600&display=swap">
<style>
  :root {
    --orange: #ee7326;
    --peach: #f4a582;
    --ink: #3a3a3a;
    --rule: #9a9a9a;
    --paper: #ffffff;
    --edge: #cfcfcf;
    --page: #ffffff;
  }
  * { box-sizing: border-box; margin: 0; padding: 0; }
  html, body { width: 1200px; height: 1101px; overflow: hidden; background: var(--page); }
  body { position: relative; font-family: "Nunito", Arial, sans-serif; color: var(--ink); }

  .letterhead, .card, .envelope { position: absolute; background: var(--paper); border: 1px solid var(--edge); }

  /* brand lockup */
  .brand { position: absolute; display: flex; align-items: center; gap: 12px; }
  .brand-dot { border-radius: 50%; background: var(--peach); flex: none; }
  .brand-name { font-weight: 600; color: var(--ink); line-height: 1.1; }

  .contact { position: absolute; border-left: 1.5px solid var(--rule); padding-left: 12px;
             font-size: 14px; line-height: 1.45; color: var(--ink); }
  .contact .icon { color: var(--orange); margin-right: 4px; }

  /* letterhead */
  .letterhead { left: 66px; top: 24px; width: 822px; height: 1050px; }
  .letterhead .brand { left: 26px; top: 34px; }
  .letterhead .brand-dot { width: 70px; height: 70px; }
  .letterhead .brand-name { font-size: 26px; width: 150px; }
  .letterhead .contact { left: 248px; top: 36px; height: 120px; }
  .letterhead-band { position: absolute; left: 0; right: 0; bottom: 0; height: 10px; background: var(--orange); }

  /* business card */
  .card { left: 912px; width: 264px; height: 159px; }
  .card-front { top: 30px; }
  .card-front .brand { left: 10px; top: 22px; gap: 8px; }
  .card-front .brand-dot { width: 34px; height: 34px; }
  .card-front .brand-name { font-size: 14px; width: 90px; }
  .card-person { position: absolute; left: 150px; top: 16px; }
  .card-name { font-size: 15px; color: var(--orange); }
  .card-role { font-size: 9px; color: var(--ink); }
  .card-details { position: absolute; left: 148px; top: 60px; width: 106px; border-top: 5px solid var(--orange);
                  padding-top: 5px; font-size: 7.5px; line-height: 1.5; }
  .card-tagline { position: absolute; left: 14px; top: 112px; font-size: 10px; color: var(--orange); font-style: italic; }
  .card-back { top: 210px; background: var(--orange); border-color: var(--orange); }
  .card-back .mark { position: absolute; left: 112px; top: 60px; width: 40px; height: 40px; border-radius: 50%; background: var(--paper); }

  /* envelope */
  .envelope { left: 369px; top: 465px; width: 807px; height: 495px; }
  .envelope-flap { position: absolute; left: 0; top: 0; width: 807px; height: 230px; }
  .envelope .brand { left: 30px; top: 250px; }
  .envelope .brand-dot { width: 70px; height: 70px; }
  .envelope .brand-name { font-size: 24px; width: 150px; }
  .envelope .contact { left: 270px; top: 280px; height: 60px; }
</style>
</head>
<body>

  <section class="letterhead" aria-label="Letterhead">
    <div class="brand">
      <span class="brand-dot"></span>
      <span class="brand-name">Sun Path &amp; Clear Way</span>
    </div>
    <address class="contact">
      48207 hwy 19 north<br>
      dalworth, ar 71482<br>
      <span class="icon">☎</span>479 555 0142<br>
      <span class="icon">✉</span>mltenbeck@mailvox.example
    </address>
    <div class="letterhead-band"></div>
  </section>

  <section class="card card-front" aria-label="Business card front">
    <div class="brand">
      <span class="brand-dot"></span>
      <span class="brand-name">Sun Path &amp; Clear Way</span>
    </div>
    <div class="card-person">
      <div class="card-name">Marla Tenbeck</div>
      <div class="card-role">Director</div>
    </div>
    <address class="card-details">
      48207 hwy 19 north<br>
      dalworth, ar 71482<br>
      479 555 0142<br>
      mltenbeck@mailvox.example
    </address>
    <p class="card-tagline">sharing good in every day</p>
  </section>

  <section class="card card-back" aria-label="Business card back">
    <span class="mark"></span>
  </section>

  <section class="envelope" aria-label="Envelope">
    <svg class="envelope-flap" viewBox="0 0 807 230" aria-hidden="true">
      <path d="M0 0 H807 L470 215 Q403 245 337 215 Z" fill="var(--orange)"/>
      <circle cx="403" cy="140" r="24" fill="var(--paper)"/>
    </svg>
    <div class="brand">
      <span class="brand-dot"></span>
      <span class="brand-name">Sun Path &amp; Clear Way</span>
    </div>
    <address class="contact">
      48207 hwy 19 north<br>
      dalworth, ar 71482
    </address>
  </section>

</body>
</html>
```